The Brambury Firm

We need a new design for our letterhead and envelopes. We are a personal injury and criminal defense firm so we need something modern and clean, but more on the professional/traditional side. Our new logo has two colors and is attached to the file so we need something that works well with those colors/matches the design. The following information needs to be on the letterhead:
Phone: (555) 314-7265
Fax: (555) 419-6032
Toll-Free: (555) 736-1149
Post Office Box 4273
Fenwick Hollow, FH 29458-4273
TQHarmClaimsDesk.example
PalmettoShieldCounsel.example

Target Market(s)

Clients, government agencies, other law firms

Industry/Entity Type

Legal

Font styles to use
Sans Serif
Other font styles liked:
• Arial

Colors

Designer to choose colors to be used in the design.

Requirements
Must have
• Must look professional and clean, modern
Nice to have
• I would like to see a design that works with the logo but does not distract from the content that will be printed on it
Should not have
• Too many colors or crazy designs.

```html
<!DOCTYPE html>
<html lang="en">
<head>
<meta charset="utf-8">
<title>The Brambury Firm – Stationery</title>
<link href="https://fonts.googleapis.com/css2?family=Arimo:wght@400;700&display=swap" rel="stylesheet">
<style>
  :root {
    --navy: #2a2878;
    --red: #d23a3c;
    --paper: #f7f7f8;
    --backdrop: #e9e6e1;
    --ink-soft: #3b3a86;
    --shadow: 0 6px 18px rgba(40, 30, 20, 0.18);
  }
  * { box-sizing: border-box; margin: 0; padding: 0; }
  html, body { width: 1200px; height: 801px; overflow: hidden; }
  body {
    background: var(--backdrop);
    font-family: "Arimo", Arial, sans-serif;
    position: relative;
  }
  .sheet { position: absolute; box-shadow: var(--shadow); }

  .wordmark {
    display: inline-flex; align-items: center; gap: 6px;
    font-weight: 700; color: var(--navy); letter-spacing: 0.02em; white-space: nowrap;
  }
  .wordmark .mark-dot { width: 9px; height: 9px; border-radius: 50%; background: var(--red); flex: none; }
  .wordmark.on-navy { color: #ffffff; }
  .wordmark.on-navy .mark-dot { background: #ffffff; }

  .folder { left: 60px; top: 250px; width: 330px; height: 440px; background: var(--navy); }
  .folder .wordmark { position: absolute; left: 22px; top: 310px; font-size: 15px; }

  .letterhead {
    left: 250px; top: 90px; width: 340px; height: 440px; background: var(--paper);
    display: flex; flex-direction: column; align-items: center;
  }
  .letterhead .wordmark { margin-top: 34px; font-size: 15px; }
  .contact-line {
    margin-top: auto; margin-bottom: 24px; padding: 0 18px;
    font-size: 6.6px; line-height: 1.6; color: var(--ink-soft); text-align: center;
    white-space: nowrap;
  }
  .contact-line .sep { margin: 0 3px; }

  .business-card {
    left: 640px; top: 90px; width: 170px; height: 100px; background: var(--paper);
    display: flex; align-items: center; justify-content: center;
  }
  .business-card .wordmark { font-size: 11px; }

  .envelope-back {
    left: 640px; top: 230px; width: 500px; height: 230px; background: var(--paper); overflow: hidden;
  }
  .envelope-back .flap { position: absolute; left: 0; top: 0; width: 100%; height: 110px; }
  .envelope-back .contact-line { position: absolute; left: 0; right: 0; bottom: 0; margin-bottom: 22px; }

  .envelope-front {
    left: 640px; top: 510px; width: 500px; height: 230px; background: var(--paper);
  }
  .envelope-front .wordmark { position: absolute; left: 24px; top: 22px; font-size: 12px; }
</style>
</head>
<body>

  <section class="sheet folder" aria-label="Presentation folder">
    <span class="wordmark on-navy"><span class="mark-dot"></span>The Brambury Firm</span>
  </section>

  <section class="sheet letterhead" aria-label="Letterhead">
    <span class="wordmark"><span class="mark-dot"></span>The Brambury Firm</span>
    <p class="contact-line">
      Phone: (555) 314-7265<span class="sep">|</span>Fax: (555) 419-6032<span class="sep">|</span>Toll-Free: (555) 736-1149<br>
      Post Office Box 4273<span class="sep">|</span>Fenwick Hollow, FH 29458-4273<br>
      TQHarmClaimsDesk.example<span class="sep">|</span>PalmettoShieldCounsel.example
    </p>
  </section>

  <section class="sheet business-card" aria-label="Business card">
    <span class="wordmark"><span class="mark-dot"></span>The Brambury Firm</span>
  </section>

  <section class="sheet envelope-back" aria-label="Envelope, back with flap">
    <svg class="flap" viewBox="0 0 500 110" preserveAspectRatio="none">
      <polygon points="0,0 500,0 500,20 250,110 0,20" fill="var(--navy)"/>
    </svg>
    <p class="contact-line">
      Phone: (555) 314-7265<span class="sep">|</span>Fax: (555) 419-6032<span class="sep">|</span>Toll-Free: (555) 736-1149<span class="sep">|</span>Post Office Box 4273<span class="sep">|</span>Fenwick Hollow, FH 29458-4273<br>
      TQHarmClaimsDesk.example<span class="sep">|</span>PalmettoShieldCounsel.example
    </p>
  </section>

  <section class="sheet envelope-front" aria-label="Envelope, front">
    <span class="wordmark"><span class="mark-dot"></span>The Brambury Firm</span>
  </section>

</body>
</html>
```